依頼詳細
お悔みに掲載された方に郵送するダイレクトメールのデザインをお願いしたいと思います。すでにホームページはありますので素材はそちらをいったん利用してもらいたいと思います。
また、レイアウトなどは添付しましたエクセルに記載しています。またスキャンした現在のダイレクトメールが入っています。
記載項目
社名/フリーダイヤル/URL/キャッチコピー/
ロゴなどは現在取り寄せ中。ホームページがあるのでそこから素材をとってください。
サイズ
A4
ページ数
両面
希望イメージ
シンプル 複雑
単色 カラフル
暗い 明るい
日常 高級
遊び心 厳粛
未来的 伝統的
女性的 男性的
希望する色
緑系、グレー系
納品ファイル
• イラストレーター形式 (.ai)
• フォトショップ形式 (.psd)
補足説明
上記のファイルのいずれか。アウトラインのあり・なしのデータをお願いします。
■ 選んだ理由

クライアントの希望にあうデザインだったためです。

■ 提案者全員のお礼・コメント

たくさんのご提案ありがとうございました。またDMやパンフレットなどのデザインコンペなど行った際には、ご参加いただければ幸いです。

宜しくお願い致します。

```html
<!DOCTYPE html>
<html lang="ja">
<head>
<meta charset="utf-8">
<title>相続税に関する大切なお知らせ</title>
<link href="https://fonts.googleapis.com/css2?family=Noto+Sans+JP:wght@400;500;700;900&family=Noto+Serif+JP:wght@600;700&display=swap" rel="stylesheet">
<style>
:root{
  --green:#6fa82e;
  --green-dark:#4f8a1f;
  --green-soft:#e9f2dc;
  --grey:#8c8c8c;
  --grey-light:#efefef;
  --orange:#e07a18;
  --text:#3a3a3a;
  --white:#ffffff;
}
*{margin:0;padding:0;box-sizing:border-box}
html,body{width:849px;height:1200px;overflow:hidden;background:var(--white)}
body{font-family:"Noto Sans JP",sans-serif;color:var(--text);position:relative}
.flyer{position:absolute;inset:0;background:var(--white)}
.header{position:absolute;left:0;top:0;width:849px;height:500px;background:linear-gradient(180deg,#dfeccd 0%,#f4f8ee 60%,#ffffff 100%)}
.notice-pill{position:absolute;left:50%;top:18px;transform:translateX(-50%);white-space:nowrap;background:var(--green);color:var(--white);font-size:15px;line-height:1.6;padding:3px 26px;border-radius:20px;letter-spacing:1px}
.headline{position:absolute;left:0;width:100%;top:62px;text-align:center;white-space:nowrap;font-family:"Noto Serif JP",serif;font-weight:700;font-size:43px;line-height:1.3;color:var(--green-dark);letter-spacing:1px}
.greeting{position:absolute;left:36px;top:150px;width:290px;font-size:12.5px;line-height:2.05;color:var(--white);background:rgba(111,168,46,.82);padding:18px 20px;border-radius:4px}
.hero-photo{position:absolute;left:336px;top:140px;width:513px;height:330px;background:linear-gradient(180deg,#cfe3ef 0%,#e6f0d8 55%,#8fbf55 100%)}
.trouble-band{position:absolute;left:36px;top:470px;width:777px;height:56px;background:var(--grey);border-radius:6px;color:var(--white);font-size:28px;font-weight:700;display:flex;align-items:center;padding-left:26px;letter-spacing:1px}
.deadline{position:absolute;left:36px;top:540px;width:500px;text-align:center;font-size:15px;color:var(--text);border-bottom:1px solid #bbb;padding-bottom:6px}
.checklist{position:absolute;left:48px;top:582px;width:480px;list-style:none}
.checklist li{display:flex;align-items:center;gap:14px;height:48px;font-size:19px;border-bottom:1px dotted #bbb}
.checklist svg{flex:none}
.aside-note{position:absolute;left:556px;top:560px;width:260px;font-size:13px;line-height:1.75;color:var(--green-dark)}
.consult-photo{position:absolute;left:556px;top:680px;width:260px;height:170px;background:linear-gradient(160deg,#f1f1ee 0%,#d9ddd3 60%,#b9c2a8 100%)}
.promises{position:absolute;left:36px;top:872px;width:777px;display:flex;gap:22px}
.promise{flex:1;height:116px;background:var(--green);color:var(--white);border-radius:14px;display:flex;align-items:center;justify-content:center;text-align:center;font-size:20px;font-weight:700;line-height:1.5}
.reserve{position:absolute;left:36px;top:1010px;width:360px;text-align:center;color:var(--orange);font-size:20px;font-weight:700;border-bottom:2px dotted var(--orange);padding-bottom:4px}
.org{position:absolute;left:36px;top:1052px;display:flex;align-items:center;gap:10px}
.org-mark{width:22px;height:22px;background:var(--green)}
.org-name{font-size:25px;font-weight:900;color:var(--green-dark)}
.org-sub{position:absolute;left:36px;top:1090px;font-size:10px;color:var(--grey)}
.tel{position:absolute;left:36px;top:1108px;font-size:40px;line-height:1.2;font-weight:900;color:var(--orange);display:flex;align-items:center;gap:6px;letter-spacing:1px}
.hours{position:absolute;left:36px;top:1160px;font-size:11px;line-height:1.5;color:var(--text)}
.ticket{position:absolute;left:430px;top:1010px;width:383px;height:172px;border:2px dashed var(--grey);border-radius:6px;padding:10px 16px}
.ticket-lead{font-size:11px;line-height:1.5;text-align:center;color:var(--text)}
.ticket-title{margin:8px auto 0;width:280px;background:var(--green);color:var(--white);text-align:center;font-size:24px;font-weight:700;border-radius:24px;padding:2px 0}
.ticket-expiry{margin-top:6px;display:flex;align-items:baseline;justify-content:center;gap:10px;font-family:"Noto Serif JP",serif;font-weight:700;color:var(--text);white-space:nowrap}
.ticket-expiry .label{font-family:"Noto Sans JP",sans-serif;font-size:14px;font-weight:500}
.ticket-expiry .year{font-size:18px}
.ticket-expiry .date{font-size:40px;line-height:1.2}
</style>
</head>
<body>
<main class="flyer">
  <section class="header">
    <p class="notice-pill">相続税や名義変更手続きに関する大切なお知らせ</p>
    <h1 class="headline">平成27年より相続税が増税されました</h1>
    <div class="hero-photo" role="img" aria-label="芝生の上で寄り添う三世代の家族の写真"></div>
    <p class="greeting">このたびはご親族様の訃報に、心よりお悔やみ申し上げます。当窓口は、新聞のお悔やみ欄を拝見しお送りさせていただきました。お辛い時期に大変恐縮ですが、相続に関するお手続きについて少しでもお力になれればと思い、ご案内申し上げます。何卒ご容赦ください。</p>
  </section>

  <h2 class="trouble-band">相続税・名義変更などでお困りではありませんか？</h2>
  <p class="deadline">一部の手続きは３ヶ月以内に行わなければいけないものがございます</p>

  <ul class="checklist">
    <li><svg width="24" height="24" viewBox="0 0 24 24"><rect x="1" y="3" width="20" height="20" fill="none" stroke="#6fa82e" stroke-width="2"/><path d="M5 12l5 5 12-14" fill="none" stroke="#e07a18" stroke-width="3"/></svg>周りに相談する人がいない</li>
    <li><svg width="24" height="24" viewBox="0 0 24 24"><rect x="1" y="3" width="20" height="20" fill="none" stroke="#6fa82e" stroke-width="2"/><path d="M5 12l5 5 12-14" fill="none" stroke="#e07a18" stroke-width="3"/></svg>相続税がかかるかの判断だけでもしてほしい</li>
    <li><svg width="24" height="24" viewBox="0 0 24 24"><rect x="1" y="3" width="20" height="20" fill="none" stroke="#6fa82e" stroke-width="2"/><path d="M5 12l5 5 12-14" fill="none" stroke="#e07a18" stroke-width="3"/></svg>相続は初めてで何をしたらいいかわからない</li>
    <li><svg width="24" height="24" viewBox="0 0 24 24"><rect x="1" y="3" width="20" height="20" fill="none" stroke="#6fa82e" stroke-width="2"/><path d="M5 12l5 5 12-14" fill="none" stroke="#e07a18" stroke-width="3"/></svg>自分で手続きをするのが不安だ</li>
    <li><svg width="24" height="24" viewBox="0 0 24 24"><rect x="1" y="3" width="20" height="20" fill="none" stroke="#6fa82e" stroke-width="2"/><path d="M5 12l5 5 12-14" fill="none" stroke="#e07a18" stroke-width="3"/></svg>役所のあいている平日になかなか休めない</li>
  </ul>

  <p class="aside-note">ご遺族様の手助けになればと思いご案内させて頂きました。相続に関連する様々な手続きを一つの窓口でまとめてお手伝いいたします。</p>
  <div class="consult-photo" role="img" aria-label="相談窓口で専門家と話す来訪者の写真"></div>

  <section class="promises">
    <p class="promise">あなたの<br>ケースに合わせて<br>サポートいたします</p>
    <p class="promise">複雑な問題も<br>それぞれの専門家と<br>解決いたします</p>
    <p class="promise">あなたにとって<br>一番よい解決方法を<br>ご提案いたします</p>
  </section>

  <footer>
    <p class="reserve">ご予約はこちらから</p>
    <div class="org"><span class="org-mark"></span><span class="org-name">緑野相続サポートセンター</span></div>
    <p class="org-sub">税理士・司法書士・行政書士による相続の総合窓口</p>
    <p class="tel"><svg width="30" height="30" viewBox="0 0 24 24"><path d="M6.6 10.8a15 15 0 006.6 6.6l2.2-2.2a1 1 0 011-.25 11.4 11.4 0 003.6.6 1 1 0 011 1V20a1 1 0 01-1 1A17 17 0 013 4a1 1 0 011-1h3.5a1 1 0 011 1 11.4 11.4 0 00.6 3.6 1 1 0 01-.25 1z" fill="#e07a18"/></svg>TEL:0120-000-000</p>
    <p class="hours">受付時間 8:00-19:00（土日祝日も受付けております）<br>〒000-0000 新緑県緑野市中央1丁目2-3</p>

    <div class="ticket">
      <p class="ticket-lead">相談無料チケットをご用意いたしました。<br>この機会に一度ご相談ください。</p>
      <p class="ticket-title">相談無料チケット</p>
      <div class="ticket-expiry"><span class="label">有効期限</span><span class="year">2018年</span><span class="date">12月12日</span></div>
    </div>
  </footer>
</main>
</body>
</html>
```